Cover for "ROOTED! The skill and rhythm of guiding teams through calm and delight"

My first book for a global audience of modern performance leaders needs its cover!
I am an international executive coach and I've developed a new approach to replace classic Performance Management with a natural, sustainable approach fit for human beings :) My first book is about this approach and serves two purposes: helping leaders and sparking their curiosity to learn more, and positioning myself as a thought leader in the field.
The book is built on personal experience; it is both professional and personal ("From me to You"), and I'd like to position it beyond classic categorisation.
Its cover should communicate humanness, naturalness, ease and joy, within an unmistakably business-y context. I would like to see designs that use the color yellow (but not sure it communicates the right things).
Updates

Target Market(s)

Leaders who aspire to have a positive impact and deliver results in a meaningful way

Industry/Entity Type

Consulting & Executive Coaching - Trusted Advisor

Font styles to use
Other font styles liked:
• Helvetica Neue

Colors
0094D4
00A9DD
6FCCEA
C7EBF8
E9F6FB
FFC000
F8CF3A
FAE287
FDF2CF
FEFAEE
EE7325
F08F49
F5BC92
FAE3D3
FDF4ED

Requirements
Must have
• A both-and feeling to it (see description), e.g., masculine AND feminine, business AND humanness. Power with, not power over...
Should not have
• Too much "bling" - no classic status symbol business success language

```html
<!DOCTYPE html>
<html lang="en">
<head>
<meta charset="utf-8">
<title>ROOTED! – Book Cover</title>
<link rel="stylesheet" href="https://fonts.googleapis.com/css2?family=Anton&family=Oswald:wght@500&display=swap">
<style>
  :root {
    --paper-light: #f4f5f6;
    --paper-shade: #e3e5e8;
    --title-red-top: #ee2a44;
    --title-red-bottom: #e6301f;
    --title-shadow: #2b2b33;
    --subtitle-red: #ee2b3d;
  }
  * { margin: 0; padding: 0; box-sizing: border-box; }
  html, body {
    width: 720px;
    height: 1200px;
    overflow: hidden;
  }
  .book-cover {
    position: relative;
    width: 720px;
    height: 1200px;
    background: linear-gradient(180deg, var(--paper-shade) 0%, var(--paper-light) 40%, var(--paper-shade) 100%);
    overflow: hidden;
  }
  .cover-title {
    position: absolute;
    top: 40px;
    left: 0;
    width: 720px;
    text-align: center;
    font-family: "Anton", "Impact", sans-serif;
    font-size: 196px;
    line-height: 1;
    letter-spacing: -2px;
    transform: scaleY(1.28);
    transform-origin: top center;
  }
  .cover-title span {
    background: linear-gradient(180deg, var(--title-red-top), var(--title-red-bottom));
    -webkit-background-clip: text;
    background-clip: text;
    color: transparent;
    filter: drop-shadow(5px 4px 0 var(--title-shadow));
  }
  .cover-photo {
    position: absolute;
    top: 330px;
    left: 0;
    width: 720px;
    height: 680px;
  }
  .cover-subtitle {
    position: absolute;
    top: 1060px;
    left: 0;
    width: 720px;
    text-align: center;
    font-family: "Oswald", "Arial Narrow", sans-serif;
    font-weight: 500;
    font-size: 34px;
    line-height: 1.35;
    color: var(--subtitle-red);
    text-transform: uppercase;
    transform: scaleY(1.1);
  }
</style>
</head>
<body>
  <main class="book-cover">
    <h1 class="cover-title"><span>ROOTED!</span></h1>

    <svg class="cover-photo" viewBox="0 0 720 680" role="img"
         aria-label="Photo of four silhouetted climbers helping each other up a rocky seaside ledge at sunset, shown through a torn-paper opening">
      <defs>
        <linearGradient id="sunsetTones" x1="0" y1="0" x2="0" y2="1">
          <stop offset="0" stop-color="#7f868c"/>
          <stop offset="0.25" stop-color="#c9b48e"/>
          <stop offset="0.45" stop-color="#efc374"/>
          <stop offset="0.6" stop-color="#6e6660"/>
          <stop offset="0.78" stop-color="#2f2220"/>
          <stop offset="1" stop-color="#1c1412"/>
        </linearGradient>
      </defs>
      <polygon class="torn-edge"
        fill="url(#sunsetTones)" stroke="#ffffff" stroke-width="3" stroke-linejoin="round"
        points="0,60 30,55 60,62 100,58 140,65 180,60 220,68 260,62 300,70 330,66 360,58 390,45 410,20 430,2 450,6 480,10 520,15 560,20 600,22 640,30 680,28 720,35
                720,560 690,570 650,575 610,600 570,610 530,620 490,640 450,630 410,650 370,645 330,665 290,660 250,678 210,670 170,660 130,665 90,650 50,655 20,645 0,650"/>
    </svg>

    <p class="cover-subtitle">The skill and rhythm of guiding<br>teams through calm and delight</p>
  </main>
</body>
</html>
```